Brochure for an engineering consultancy

We need a brochure design for our engineering consulting business. We basically deal with ground-related works (i.e. foundations, drill rigs, excavators, road embankments...etc). We have two main aspects of our work. They are as following:
1- Design Services: this is related to office work like calculations, drawings and engineering tools and software.
2- Construction Support Services: outdoor work where we go to construction sites and supervise and watch the projects being built onsite.
3- Ground investigations where we test the ground to know how strong it is for building
Please have a look at our website www.pelvarco.com.au for an idea of whet we do. You can use materials from the website for this brochure only.
We are after a simple but yet very attractive brochure to suit both office-minded people and construction-minded people. We have prepared some symbols that we would like to use on the brochure in addition to the attached photos. Those are symbols we created so please, do not use them on other projects.
The winning design the one that would succeed in reflecting professionalism, trustworthiness and helpfulness. Please remember, we make money out of engineering ADVICE and KNOWLEDGE.
Our logo is also attached. Include blue colour please. Also A4 single fold please.
Target Market(s)
construction companies, buildings developers and engineering consultants
Industry/Entity Type
Business
Requirements
Must have
- all 3 of our services in this order
- 1- Construction support services
- 2- Ground investigation services
- 3- Design services
Should not have
- Excessive presence of excavators and earthmoving machines. From our experience brochure designers think we are an excavator hiring company or that we are earthmoving contractors. We are not. We are an engineering consultant

```html
<!DOCTYPE html>
<html lang="en">
<head>
<meta charset="utf-8">
<title>Pelvarco Engineers – Brochure Outside</title>
<link rel="stylesheet" href="https://fonts.googleapis.com/css2?family=Michroma&family=Rajdhani:wght@500;600;700&family=Titillium+Web:wght@400;600&display=swap">
<style>
  :root {
    --blue: #1457c8;
    --blue-deep: #0b3fa8;
    --blue-light: #2f7de6;
    --navy: #0d3d8f;
    --grey: #8f9398;
    --paper: #f3f4f5;
    --ink: #2a2c30;
    --white: #ffffff;
  }
  html, body { margin: 0; padding: 0; overflow: hidden; }
  body { width: 1200px; height: 886px; background: #e9e9ea; }
  .spread { position: relative; width: 1200px; height: 886px; overflow: hidden; }

  .panel-back { position: absolute; left: 0; top: 0; width: 600px; height: 886px;
    background: linear-gradient(160deg, #e4e5e7 0%, #f4f5f6 45%, #eeeff0 100%); }
  .panel-front { position: absolute; left: 600px; top: 0; width: 600px; height: 886px; background: var(--white); }

  .cover-photo { position: absolute; left: 0; top: 118px; width: 600px; height: 540px;
    background: radial-gradient(ellipse at 70% 25%, #f6e4c2 0%, #d9a968 30%, #8a5a33 65%, #4a3322 100%); }

  .bands { position: absolute; left: 0; top: 0; width: 1200px; height: 886px; }

  .pill { position: absolute; left: 50%; transform: translateX(-50%); margin: 0;
    background: var(--blue-deep); color: var(--white); border-radius: 14px;
    font: 700 21px/1 "Rajdhani", sans-serif; letter-spacing: 0.5px; padding: 4px 14px; white-space: nowrap; }
  .pill::before, .pill::after { content: "•"; font-size: 14px; margin: 0 8px; vertical-align: 3px; }
  .pill-about { top: 30px; }
  .pill-services { top: 400px; }

  .copy { position: absolute; left: 24px; width: 552px; color: var(--ink);
    font: 400 13.6px/1.45 "Titillium Web", sans-serif; text-align: justify; }
  .copy p { margin: 0 0 10px; }
  .copy strong { font-weight: 600; color: #111; }
  .copy-about { top: 74px; }
  .copy-services { top: 440px; }

  .contact { position: absolute; right: 637px; top: 656px; text-align: right; color: var(--white);
    font: 500 14.5px/1 "Rajdhani", sans-serif; letter-spacing: 0.6px; }
  .contact h2 { margin: 0 0 14px; font: 600 28px/1 "Rajdhani", sans-serif; letter-spacing: 1.5px; }
  .contact .company { font-size: 16px; font-weight: 600; margin-bottom: 11px; margin-right: 4px; }
  .contact .line { margin-bottom: 11px; display: flex; justify-content: flex-end; align-items: center; gap: 7px; }
  .contact svg { width: 12px; height: 12px; fill: var(--white); }
  .social { display: flex; justify-content: flex-end; align-items: center; gap: 9px; margin-top: 4px; }
  .social span.dot { width: 15px; height: 15px; border-radius: 50%; background: var(--white); display: inline-block; }

  .brand-name { font: 700 30px/1 "Rajdhani", sans-serif; letter-spacing: 3px; color: var(--white); }
  .brand-back { position: absolute; left: 22px; top: 818px; display: flex; align-items: center; gap: 10px; }
  .brand-back .mark { width: 28px; height: 28px; background: var(--white); }

  .brand-front { position: absolute; left: 0; width: 600px; top: 30px; display: flex; justify-content: center; align-items: center; gap: 18px; }
  .brand-front .mark { width: 62px; height: 62px; background: var(--blue); }
  .brand-front .brand-name { color: var(--blue); font-size: 62px; letter-spacing: 6px; }

  .front-layer { position: absolute; left: 600px; top: 0; width: 600px; height: 886px; }
  .headline { position: absolute; left: 0; width: 600px; top: 696px; text-align: center; margin: 0; }
  .headline .big, .headline .small { display: block; font-family: "Michroma", sans-serif; text-transform: uppercase;
    background: linear-gradient(180deg, #ffffff 0%, #d7dbe0 45%, #8e959d 55%, #eef0f2 100%);
    -webkit-background-clip: text; background-clip: text; color: transparent; }
  .headline .big { font-size: 48px; line-height: 1.1; letter-spacing: 1px; }
  .headline .small { font-size: 26.5px; line-height: 1.3; margin-top: 4px; }
  .front-url { position: absolute; left: 0; width: 600px; top: 831px; text-align: center; color: var(--white);
    font: 600 18px/1 "Rajdhani", sans-serif; letter-spacing: 0.8px; }
</style>
</head>
<body>
<main class="spread">
  <section class="panel-back">
    <h2 class="pill pill-about">ABOUT US</h2>
    <div class="copy copy-about">
      <p><strong>Pelvarco Engineers Pty Ltd</strong> is a ground engineering &amp; geotechnical consultancy working in the field of design &amp; construction with speciality areas of piling, shoring &amp; earth works. Our staff have the knowledge, experience and skills to be available on the ground to service your project at anytime.</p>
      <p>Our great relationship with our clients is due to the skills, experience &amp; character of our staff, many of whom carry postgraduate degrees &amp; the status of chartered professional engineer.</p>
      <p>Our approach to solving problems is to come up with simple, cost effective, high quality &amp; achievable solutions. We always succeed to deliver high quality solutions with minimum delays to our clients' work.</p>
      <p>We work on a solid practical &amp; scientific basis which has allowed us to stand out between others. We are well aware of the requirements of local authorities &amp; main government bodies which guarantees a smoother progress of our clients' projects.</p>
    </div>
    <h2 class="pill pill-services">SERVICES</h2>
    <div class="copy copy-services">
      <p>Our services include design, construction support (site inspections) &amp; ground testing &amp;certification for variety of projects including piling, shoring &amp; earthworks. We do provide services from A to Z when it comes to ground engineering &amp; geotechnical advice. We operate with the most up to date Australian &amp; international standards as well as the most modern design &amp; testing tools and software. We are confident our advice is always easily achievable, reasonable &amp; practical. We never compromise on safety neither provide half solutions.</p>
    </div>
  </section>

  <section class="panel-front">
    <div class="brand-front"><span class="mark"></span><span class="brand-name">PELVARCO</span></div>
    <div class="cover-photo" role="img" aria-label="Photo of a white hard hat, rolled plans and glasses on a desk with engineers working in a bright office behind"></div>
  </section>

  <svg class="bands" viewBox="0 0 1200 886" aria-hidden="true">
    <defs>
      <linearGradient id="band-blue" x1="0" y1="0" x2="1" y2="1">
        <stop offset="0" stop-color="#2a72e0"/>
        <stop offset="1" stop-color="#0c44b0"/>
      </linearGradient>
    </defs>
    <polygon points="64,571 64,600 180,657" fill="#9a9ea4"/>
    <polygon points="0,593 180,657 600,570 600,886 0,886" fill="url(#band-blue)"/>
    <polygon points="0,593 180,657 0,720" fill="#3d8cf0" opacity="0.55"/>
    <polygon points="180,657 320,886 0,886 0,720" fill="#1a5fd0" opacity="0.5"/>
    <polygon points="1138,574 1138,598 1026,657" fill="#9a9ea4"/>
    <polygon points="600,570 1026,657 1200,593 1200,886 600,886" fill="url(#band-blue)"/>
    <polygon points="1026,657 1200,593 1200,640" fill="#3d8cf0" opacity="0.55"/>
    <polygon points="1026,657 960,886 1200,886 1200,640" fill="#0a3c9e" opacity="0.45"/>
  </svg>

  <address class="contact">
    <h2>CONTACT US</h2>
    <div class="company">PELVARCO ENGINEERS PTY LTD</div>
    <div class="line"><svg viewBox="0 0 12 12"><path d="M6 0a4 4 0 0 0-4 4c0 3 4 8 4 8s4-5 4-8a4 4 0 0 0-4-4zm0 5.6A1.6 1.6 0 1 1 6 2.4a1.6 1.6 0 0 1 0 3.2z"/></svg>48 Harlow Street, Kelmont, NSW 2150</div>
    <div class="line"><svg viewBox="0 0 12 12"><path d="M2.5 0.5l2 2.4-1.1 1.3c.8 1.6 2 2.9 3.6 3.6l1.3-1.1 2.4 2-1 2.3C5 11 1 7 .3 1.5z"/></svg>0400 555 018</div>
    <div class="line"><svg viewBox="0 0 12 12"><path d="M0 2h12v8H0zM0.8 2.6L6 6.6l5.2-4V3.4L6 7.4 0.8 3.4z"/></svg>info@pelvarco.com.au</div>
    <div class="line"><svg viewBox="0 0 12 12"><path d="M6 0a6 6 0 1 0 0 12A6 6 0 0 0 6 0zm0 1c.9 0 1.7 1.9 1.9 4.5H4.1C4.3 2.9 5.1 1 6 1zM1 6.5h2.1c.1 1.7.4 3.1.9 4A5 5 0 0 1 1 6.5zm0-1a5 5 0 0 1 3-4c-.5.9-.8 2.3-.9 4zm5 5.5c-.9 0-1.7-1.9-1.9-4.5h3.8C7.7 9.1 6.9 11 6 11zm2-.5c.5-.9.8-2.3.9-4H11a5 5 0 0 1-3 4zm.9-5c-.1-1.7-.4-3.1-.9-4a5 5 0 0 1 3 4z"/></svg>www.pelvarco.com.au</div>
    <div class="social">Follow Us :<span class="dot"></span><span class="dot"></span><span class="dot"></span><span class="dot"></span><span class="dot"></span></div>
  </address>

  <div class="brand-back"><span class="mark"></span><span class="brand-name">PELVARCO</span></div>

  <div class="front-layer">
    <h1 class="headline"><span class="big">The Ground</span><span class="small">Engineering Experts</span></h1>
    <div class="front-url">www.pelvarco.com.au</div>
  </div>
</main>
</body>
</html>
```